Brochure Design- Targeted at Property Developers

We are the largest Conveyancing (property law) firm in the state of Victoria, Australia.

We need a very sophisticated brochure to enable us to take the next step and compete with law firms for property developer clients.

Much about us can be found on our website (inlcuding logos, photos, etc) www.brindlecove.com.au but our business name is Brindlecove- Marlow Reach not just Brindlecove. ALSO I HAVE ATTACHED MANY PHOTOS OF OUR STAFF AND SOME LOGOS TO HELP!!

Size: fold (A3 double sided so that there is 4 A4 pages)

Copy:

This can be played with by the designer to spread across the 4 pages. Ideally the front page will be very minimalistic and not mention our brand (or at least the brand should not dominate):

Page 1: Do property developers have a genuine alternative to high legal fees?

Page 2 and 3:

- 100% of our developer clients recommend us
- We already look after the Conveyancing needs of more developers in Victoria than any other Conveyancing firm
- Industry benchmark off- the- plan contracts (tailored to the requirements of each development). Our special conditions (including variations, rebates and resale restrictions) are carefully chosen to protect the interests of our vendors while being commercially sensitive to ensure sales are not lost unnecessarily
- Expert in guiding developers from first time dual occupancies to seasoned developers of large scale land and highrise projects
- Our large team and highly refined systems ensure fastest possible settlement times after subdivision registration
- We are available to train your project marketers on completing and executing contracts so that sales are not delayed or lost
- Establishment of interest bearing trust accounts
- Before you buy a development site have us thoroughly investigate the contract and vendors statement. We can then conduct the purchase settlement on your behalf.
- We have the friendliest and most efficient staff. Every dealing you have with our dedicated Development Division will be prompt, professional and impressive. You will never need to follow us up!
- Highly experienced Conveyancers with the security of full Solicitor support

Please consider us next time you need Conveyancing.

Services options:
- Use us from contract preparation to settlement or;
- Have your Solicitor prepare the contract and use us as an alternative for the settlement stage only. Many Solicitors recommend us for this service already
- Fast subdivision lodgements (including obtaining mortgagee’s consent, Solicitor preparation of Land Titles Office application, owners corporation establishment)

Page 4: Just our contact details (see our website)

The design should make us look highly professional, conservative, yet cutting edge.
Updates

Target Market(s)

Property developers of small to medium sized land and unit developments

Industry/Entity Type

Security

Requirements
Must have
• - Our logo and contact details as well as the copy above.
Nice to have
• - Pictures of land sites, highrise buildings under construction
Should not have
• I really dislike overly corny photos where everyone is fake and smiling. Other photos would be great but not too cheesy.

```html
<!DOCTYPE html>
<html lang="en">
<head>
<meta charset="utf-8">
<title>Brindlecove – Property Conveyancing Specialists</title>
<link href="https://fonts.googleapis.com/css2?family=Tinos:wght@400;700&display=swap" rel="stylesheet">
<style>
  :root {
    --backdrop: #b3b8ad;
    --olive: #9c984c;
    --paper: #ffffff;
    --ink: #1c1c1c;
    --portrait: #4a3a33;
  }
  * { margin: 0; padding: 0; box-sizing: border-box; }
  html, body { width: 1200px; height: 849px; overflow: hidden; background: var(--backdrop); }
  .spread { position: relative; width: 1200px; height: 849px; font-family: "Tinos", "Times New Roman", serif; color: var(--ink); }
  .panel { position: absolute; background: var(--paper); }
  .band-h { position: absolute; left: 0; top: 94px; width: 1200px; height: 63px; background: var(--olive); }
  .band-v { position: absolute; left: 582px; top: 0; width: 44px; height: 849px; background: var(--olive); }
  .masthead-left { left: 15px; top: 22px; width: 567px; height: 72px; }
  .masthead-right { left: 626px; top: 22px; width: 543px; height: 72px; }
  .page-left { left: 15px; top: 157px; width: 567px; height: 673px; }
  .page-right { left: 626px; top: 157px; width: 543px; height: 673px; }
  .brand-title { position: absolute; left: 35px; top: 41px; font-size: 22px; line-height: 28px; color: var(--olive); font-weight: 400; }
  .section-heading { position: absolute; font-size: 18px; line-height: 22px; font-weight: 400; color: var(--olive); white-space: nowrap; }
  .copy { position: absolute; font-size: 10.4px; line-height: 12px; white-space: nowrap; }
  .copy p { margin-bottom: 12px; }
  .photo { position: absolute; }
  .photo-house { left: 304px; top: 171px; width: 268px; height: 201px; background: linear-gradient(180deg, #4e86c0 0%, #a8c4dc 55%, #4d7a3a 80%, #3f6a2e 100%); }
  .photo-skyline { left: 28px; top: 380px; width: 270px; height: 175px; background: linear-gradient(180deg, #8fb6d8 0%, #c9d7df 40%, #9aa39a 55%, #5f8a45 75%, #4c7a36 100%); }
  .photo-tower { left: 28px; top: 572px; width: 270px; height: 243px; background: linear-gradient(135deg, #c7d2dc 0%, #8e9aa4 45%, #5d6a74 75%, #3f4a52 100%); }
  .photo-portrait { left: 942px; top: 171px; width: 211px; height: 318px; background: linear-gradient(180deg, #6e5a4e 0%, var(--portrait) 50%, #231c1a 100%); }
  .photo-site { left: 644px; top: 537px; width: 285px; height: 277px; background: linear-gradient(180deg, #a9b2c8 0%, #d1d3dc 35%, #9b6a55 55%, #6c8a3e 70%, #3f6a25 100%); }
  .photo-highrise { left: 946px; top: 537px; width: 208px; height: 274px; background: linear-gradient(180deg, #9fc0dc 0%, #dde6ee 35%, #6b7268 65%, #9a958a 100%); }
</style>
</head>
<body>
<main class="spread">
  <div class="band-v"></div>
  <div class="band-h"></div>

  <header class="panel masthead-left"></header>
  <header class="panel masthead-right"></header>
  <h1 class="brand-title">Property Conveyancing Specialists</h1>

  <section class="panel page-left"></section>
  <section class="panel page-right"></section>

  <h2 class="section-heading" style="left:34px; top:177px;">What We Do</h2>
  <div class="copy" style="left:34px; top:218px;">
    <p>Buying or selling real estate involves a large investment of<br>finances and time. So, you want to make sure the details are<br>handled by professionals. Brindlecove - the Property<br>Conveyancing Specialists - take care of your property<br>transactions from beginning to end, so your whole experience<br>is seamless and stress-free.</p>
    <p>Our services are backed up by our own legal department,<br>so your security and peace of mind is guaranteed. We also<br>give you the one-on-one personal attention you deserve.</p>
  </div>

  <div class="photo photo-house" role="img" aria-label="Photo of a weatherboard house with palm trees and lawn under a blue sky"></div>
  <div class="photo photo-skyline" role="img" aria-label="Photo of a city skyline beyond green parkland"></div>
  <div class="photo photo-tower" role="img" aria-label="Photo looking up at a glass high-rise office tower"></div>

  <h2 class="section-heading" style="left:312px; top:380px;">So Why Choose Us?</h2>
  <div class="copy" style="left:308px; top:408px;">
    <p>- 100% of our developer clients recommend us.</p>
    <p>- We already look after the Conveyancing needs of more<br>developers in Victoria than any other Conveyancing firm.</p>
    <p>- Industry benchmark off- the- plan contracts (tailored to<br>the requirements of each development). Our special conditions<br>(including variations, rebates and resale restrictions) are carefully<br>chosen to protect the interests of our vendors while being<br>commercially sensitive to ensure sales are not lost unnecessarily.</p>
    <p>- Expert in guiding developers from first time dual occupancies<br>to seasoned developers of large scale land and highrise projects.</p>
    <p>- Our large team and highly refined systems ensure fastest<br>possible settlement times after subdivision registration.</p>
    <p>- We are available to train your project marketers on<br>completing and executing contracts so that sales are not delayed<br>or lost.</p>
    <p>- Establishment of interest bearing trust accounts.</p>
    <p>- Before you buy a development site have us thoroughly<br>investigate the contract and vendors statement. We can then<br>conduct the purchase settlement on your behalf.</p>
    <p>- We have the friendliest and most efficient staff. Every dealing<br>you have with our dedicated Development Division will be<br>prompt, professional and impressive. You will never need to<br>follow us up!</p>
    <p>- Highly experienced Conveyancers with the security of full<br>Solicitor support.</p>
  </div>

  <h2 class="section-heading" style="left:657px; top:179px;">Conveyancing Services We Offer</h2>
  <div class="copy" style="left:657px; top:216px;">
    <p>- Use us from contract preparation to settlement or;</p>
    <p>- Have your Solicitor prepare the contract and use us as an<br>alternative for the settlement stage only. Many Solicitors<br>recommend us for this service already.</p>
    <p>- Fast subdivision lodgements (including obtaining mortgagee’s<br>consent, Solicitor preparation of Land Titles Office application,<br>owners corporation establishment).</p>
    <p>- Property Purchases</p>
    <p>- Property Sales</p>
    <p>- Business Services</p>
    <p>&nbsp;- Related Parties Title Transfer</p>
    <p>&nbsp;- Deceased Estate</p>
    <p>&nbsp;- Executors or Beneficiaries</p>
    <p>And more, please see our website for a full list of our Services<br>or see the contact details on the rear of the brochure to contact us<br>directly.</p>
  </div>

  <div class="photo photo-portrait" role="img" aria-label="Portrait photo of a staff member with dark hair"></div>
  <div class="photo photo-site" role="img" aria-label="Photo of a building under construction with a crane beside a lawn"></div>
  <div class="photo photo-highrise" role="img" aria-label="Photo of a high-rise tower under construction above a street"></div>
</main>
</body>
</html>
```